Marrowfield Contracting Business Cards

Front of card:

Full Logo
Name
Address
Office Phone
Cell Phone
Email
Website

Back:
Logo Mark in background
List and markets and services performed

```html
<!DOCTYPE html>
<html lang="en">
<head>
<meta charset="utf-8">
<title>Marrowfield Contracting Business Cards</title>
<link rel="stylesheet" href="https://fonts.googleapis.com/css2?family=Open+Sans:wght@300;400;700&display=swap">
<style>
  :root {
    --brand-red: #db2327;
    --brand-red-deep: #c11d21;
    --slate-grey: #78787a;
    --paper-white: #ffffff;
    --backdrop: #f3f0f0;
    --text-light: #f4f4f4;
  }
  * { box-sizing: border-box; margin: 0; padding: 0; }
  html, body {
    width: 1199px;
    height: 1200px;
    overflow: hidden;
    background: var(--backdrop);
    font-family: "Open Sans", Arial, sans-serif;
  }
  .card {
    position: absolute;
    left: 165px;
    width: 872px;
    height: 512px;
    background: var(--brand-red);
    overflow: hidden;
  }
  .card--front { top: 50px; }
  .card--back { top: 631px; }

  .info-band {
    position: absolute;
    left: 260px;
    top: 60px;
    right: 0;
    height: 393px;
    background: var(--slate-grey);
    border-radius: 197px 0 0 197px;
  }
  .logo-ring {
    position: absolute;
    left: 59px;
    top: 96px;
    width: 336px;
    height: 336px;
    border-radius: 50%;
    border: 2px solid var(--brand-red);
  }
  .logo-disc {
    position: absolute;
    left: 64px;
    top: 101px;
    width: 322px;
    height: 322px;
    border-radius: 50%;
    background: var(--paper-white);
    display: flex;
    align-items: center;
    justify-content: center;
    text-align: center;
  }
  .logo-name {
    color: var(--brand-red);
    font-weight: 700;
    font-size: 27px;
    line-height: 1.2;
    text-transform: uppercase;
    letter-spacing: 1px;
  }

  .holder {
    position: absolute;
    right: 56px;
    top: 142px;
    text-align: right;
    color: var(--text-light);
  }
  .holder-name {
    font-size: 32px;
    font-weight: 300;
    letter-spacing: 0.5px;
    line-height: 1.1;
  }
  .holder-name strong { font-weight: 700; }
  .holder-role {
    font-size: 23px;
    font-weight: 300;
    margin-top: 8px;
  }

  .contact-list {
    position: absolute;
    right: 60px;
    top: 240px;
    list-style: none;
    color: var(--text-light);
    font-size: 19px;
    font-weight: 300;
    text-align: right;
  }
  .contact-list li {
    height: 33px;
    display: flex;
    align-items: center;
    justify-content: flex-end;
    gap: 14px;
  }
  .contact-icon { width: 16px; height: 16px; flex: none; }

  .back-mark {
    position: absolute;
    left: 138px;
    top: 168px;
    display: flex;
    align-items: center;
    gap: 36px;
  }
  .back-disc {
    width: 176px;
    height: 176px;
    border-radius: 50%;
    background: var(--brand-red-deep);
  }
  .back-name {
    color: var(--brand-red-deep);
    font-weight: 700;
    font-size: 36px;
    line-height: 1.1;
    text-transform: uppercase;
    letter-spacing: 1px;
  }

  .services {
    position: absolute;
    left: 0;
    right: 0;
    top: 394px;
    text-align: center;
    color: var(--text-light);
  }
  .services-title {
    font-size: 15px;
    font-weight: 700;
    letter-spacing: 2px;
    text-transform: uppercase;
    margin-bottom: 8px;
  }
  .services-list {
    list-style: none;
    font-size: 16px;
    font-weight: 300;
    line-height: 1.6;
  }
  .services-list li { display: inline; }
  .services-list li + li::before { content: "\00B7"; margin: 0 10px; }
</style>
</head>
<body>

<section class="card card--front" aria-label="Card front">
  <div class="info-band"></div>
  <div class="logo-ring"></div>
  <div class="logo-disc">
    <span class="logo-name">Marrowfield<br>Contracting</span>
  </div>

  <div class="holder">
    <p class="holder-name">DORIAN <strong>VALE HARTLEY</strong></p>
    <p class="holder-role">Managing Member</p>
  </div>

  <ul class="contact-list">
    <li>(075) 3190 4426
      <svg class="contact-icon" viewBox="0 0 16 16" aria-hidden="true"><rect x="4" y="1" width="8" height="14" rx="1.5" fill="none" stroke="#f4f4f4" stroke-width="1.5"/><circle cx="8" cy="12.5" r="0.9" fill="#f4f4f4"/></svg>
    </li>
    <li>1234 600 781
      <svg class="contact-icon" viewBox="0 0 16 16" aria-hidden="true"><path d="M4 1.5l2.4 3-1.5 1.7c.8 1.9 2.3 3.4 4.2 4.2l1.7-1.5 3 2.4-1.3 2.6C7 13.6 2.4 9 1.8 3.1z" fill="#f4f4f4"/></svg>
    </li>
    <li>info@marrowfieldcontracting.com
      <svg class="contact-icon" viewBox="0 0 16 16" aria-hidden="true"><rect x="1" y="3.5" width="14" height="9" fill="#f4f4f4"/><path d="M1 3.5l7 5 7-5" fill="none" stroke="#78787a" stroke-width="1.2"/></svg>
    </li>
    <li>www.marrowfieldcontracting.com
      <svg class="contact-icon" viewBox="0 0 16 16" aria-hidden="true"><circle cx="8" cy="8" r="6.5" fill="#f4f4f4"/><path d="M4 5c2 0 2 2 4 2s1 3-1 3-1 3-2 3M10 3c0 2 2 2 3 3" fill="none" stroke="#78787a" stroke-width="1.1"/></svg>
    </li>
    <li>2180 Quarry Lane, Suite 4, Alder Falls
      <svg class="contact-icon" viewBox="0 0 16 16" aria-hidden="true"><path d="M8 15s-5-5.2-5-8.8A5 5 0 0 1 13 6.2C13 9.8 8 15 8 15z" fill="#f4f4f4"/><circle cx="8" cy="6.2" r="1.8" fill="#78787a"/></svg>
    </li>
  </ul>
</section>

<section class="card card--back" aria-label="Card back">
  <div class="back-mark">
    <div class="back-disc"></div>
    <span class="back-name">Marrowfield<br>Contracting<br>LLC</span>
  </div>

  <div class="services">
    <p class="services-title">Markets &amp; Services</p>
    <ul class="services-list">
      <li>Commercial</li><li>Residential</li><li>Industrial</li><li>Site Work</li>
    </ul>
    <ul class="services-list">
      <li>General Contracting</li><li>Renovation</li><li>Concrete</li><li>Project Management</li>
    </ul>
  </div>
</section>

</body>
</html>
```